Graphic to hang inside of fitness studio

This graphic will be printed on vinyl and hung inside of a boutique fitness studio for 2019. Graphic should read YEAR OF POSSIBILITIES.

2018 was called Year of Living Well. We would like something on trend for 2019 to hang within the studio as our 2019 Mantra. It is not a logo but for internal use. I've attached our logo here and the website is www.quillenmovehall.com for additional reference. Thank you.

Target Market(s)

25 to 45 women

Industry/Entity Type

Fitness

Colors

Designer to choose colors to be used in the design.

Requirements
Must have
• On trend for 2019. (no people in image)
• Year of Possibilities in trendy font.
• Easy to read.
• Need text only.
• Do not need graphic images.
Nice to have
• Tintavo colours for 2019
• 2019 design trends for background
Should not have
• Male dominate colour or masculine traits.
• Photos of fitness.
• Photos of people.
• Photos of equipment.

```html
<!DOCTYPE html>
<html lang="en">
<head>
<meta charset="utf-8">
<title>Year of Possibilities</title>
<link rel="stylesheet" href="https://fonts.googleapis.com/css2?family=Londrina+Solid:wght@400;900&display=swap">
<style>
  :root {
    --sky-deep: #17527f;
    --sky-mid: #2f86b0;
    --sky-haze: #8fcbd8;
    --sea-deep: #1a9fae;
    --sea-bright: #3fd3cf;
    --surf: #bfeee6;
    --sand: #f1e7d2;
    --sand-light: #f6eedd;
    --lettering: #f4ead7;
  }
  html, body {
    margin: 0;
    padding: 0;
    width: 1200px;
    height: 675px;
    overflow: hidden;
    background: var(--sand);
  }
  .mantra-poster {
    position: relative;
    width: 1200px;
    height: 675px;
    overflow: hidden;
  }
  .beach-backdrop {
    position: absolute;
    inset: 0;
    width: 1200px;
    height: 675px;
    display: block;
  }
  .mantra-title {
    position: absolute;
    inset: 0;
    margin: 0;
    font-family: "Londrina Solid", "Arial Narrow", sans-serif;
    font-weight: 400;
    color: var(--lettering);
    text-align: center;
    line-height: 1;
  }
  .mantra-line {
    position: absolute;
    left: 0;
    right: 0;
    display: flex;
    justify-content: center;
    align-items: center;
    white-space: nowrap;
  }
  .mantra-line--top {
    top: 97px;
    font-size: 141px;
    letter-spacing: 11px;
  }
  .mantra-line--top .mantra-words { margin-right: -11px; }
  .mantra-line--bottom {
    top: 266px;
    font-size: 132px;
    letter-spacing: 12px;
    padding-left: 12px;
  }
  .star-row {
    position: relative;
    top: 33px;
    display: flex;
    gap: 9px;
    font-size: 40px;
    letter-spacing: 0;
  }
  .star-row--left { margin-right: 8px; }
  .star-row--right { margin-left: 8px; }
</style>
</head>
<body>
  <main class="mantra-poster">
    <svg class="beach-backdrop" viewBox="0 0 1200 675" role="img"
         aria-label="Photograph of a tropical beach under a blue sky with white clouds, turquoise sea, and paper origami boats in red, blue and aqua on the sand">
      <defs>
        <linearGradient id="beachGradient" x1="0" y1="0" x2="0" y2="1">
          <stop offset="0" stop-color="var(--sky-deep)"/>
          <stop offset="0.35" stop-color="var(--sky-mid)"/>
          <stop offset="0.58" stop-color="var(--sky-haze)"/>
          <stop offset="0.595" stop-color="var(--sea-deep)"/>
          <stop offset="0.68" stop-color="var(--sea-bright)"/>
          <stop offset="0.76" stop-color="var(--surf)"/>
          <stop offset="0.82" stop-color="var(--sand-light)"/>
          <stop offset="1" stop-color="var(--sand)"/>
        </linearGradient>
      </defs>
      <rect width="1200" height="675" fill="url(#beachGradient)"/>
    </svg>

    <h1 class="mantra-title">
      <span class="mantra-line mantra-line--top">
        <span class="star-row star-row--left" aria-hidden="true"><span>★</span><span>★</span><span>★</span><span>★</span></span>
        <span class="mantra-words">YEAR OF</span>
        <span class="star-row star-row--right" aria-hidden="true"><span>★</span><span>★</span><span>★</span><span>★</span></span>
      </span>
      <span class="mantra-line mantra-line--bottom">POSSIBILITIES</span>
    </h1>
  </main>
</body>
</html>
```